Business Card Design Project

My business sells promotional merchandise to large blue chip companies. Gear like polo shirts, drink bottles, pens, basically anything that you can put a company logo onto.

I need the following elements included:
Logo as attached
Peter Hallorand Managing Director
21 Kestrel Court Thornlea 4168
mobile 0438 612054
email tidewell@tidewellcoastal.com.au

Promotional Merchandise with a difference

Mature age Marketing Managers

Business

```html
<!DOCTYPE html>
<html lang="en">
<head>
<meta charset="utf-8">
<title>Tidewell Business Cards</title>
<link href="https://fonts.googleapis.com/css2?family=Questrial&display=swap" rel="stylesheet">
<style>
  :root {
    --board: #d3d8d8;
    --blue-deep: #1a1fc8;
    --blue-main: #2a35ef;
    --blue-light: #4d6bff;
    --ink-blue: #2730e6;
    --ink-grey: #2e2e2e;
    --white: #ffffff;
    --mist: #e6e9ea;
  }
  * { margin: 0; padding: 0; box-sizing: border-box; }
  html, body { width: 1200px; height: 753px; overflow: hidden; }
  body {
    background: var(--board);
    font-family: "Questrial", "Century Gothic", sans-serif;
    position: relative;
  }
  .card {
    position: absolute;
    width: 586px;
    height: 334px;
    overflow: hidden;
  }
  .card--front { background: var(--blue-deep); }
  .card--back { background: var(--white); }
  .row-top .card { top: 38px; }
  .row-bottom .card { top: 381px; }
  .col-left { left: 11px; }
  .col-right { left: 603px; }

  .front-art {
    position: absolute;
    inset: 0;
    background: radial-gradient(ellipse at 45% 40%, var(--blue-main) 0%, var(--blue-deep) 80%);
  }

  .front-logo {
    position: absolute;
    left: 0; right: 0;
    text-align: center;
    color: var(--white);
    font-size: 66px;
    letter-spacing: 3px;
    line-height: 1;
  }
  .front-tagline {
    position: absolute;
    left: 0; right: 0;
    text-align: center;
    font-size: 14px;
  }
  .tagline-band {
    position: absolute;
    left: 0; right: 0;
    top: 184px;
    height: 16px;
    background: var(--white);
    color: var(--ink-blue);
    font-size: 14px;
    line-height: 16px;
    text-align: center;
  }
  .row-top .front-logo { top: 100px; }
  .row-bottom .front-logo { top: 121px; }
  .row-bottom .front-tagline { top: 204px; color: var(--white); }

  .mist {
    position: absolute;
    left: 40px; top: 20px;
    width: 500px; height: 260px;
    background: radial-gradient(ellipse at 45% 50%, var(--mist) 0%, rgba(230,233,234,0.5) 45%, rgba(255,255,255,0) 72%);
  }
  .back-logo {
    position: absolute;
    left: 32px; top: 121px;
    font-size: 46px;
    color: var(--ink-blue);
    letter-spacing: 1px;
    line-height: 1;
  }
  .logo-bar {
    position: absolute;
    left: 271px; top: 135px;
    width: 260px; height: 23px;
    background: linear-gradient(90deg, var(--ink-blue) 0%, var(--blue-light) 45%, rgba(77,107,255,0) 100%);
  }
  .person {
    position: absolute;
    right: 58px; top: 78px;
    text-align: right;
  }
  .person-name { font-size: 28px; color: var(--ink-blue); line-height: 1.1; }
  .person-title { font-size: 15px; color: var(--ink-grey); line-height: 1.05; }
  .contact {
    position: absolute;
    left: 279px; top: 167px;
    list-style: none;
    font-size: 16px;
    letter-spacing: 0.3px;
    color: var(--ink-grey);
    line-height: 18px;
  }
  .contact li { display: flex; align-items: center; gap: 5px; }
  .contact svg { width: 15px; height: 13px; fill: var(--ink-grey); }
  .website {
    position: absolute;
    left: 0; right: 0;
    top: 276px;
    text-align: center;
    font-size: 18px;
    letter-spacing: 3.6px;
    color: var(--ink-blue);
  }
</style>
</head>
<body>

<section class="row-top">
  <article class="card card--front col-left">
    <div class="front-art" role="img" aria-label="Deep blue abstract background with soft light"></div>
    <div class="front-logo">TIDEWELL</div>
    <div class="tagline-band">Promotional Merchandise with a difference</div>
  </article>

  <article class="card card--back col-right">
    <div class="mist" role="img" aria-label="Soft pale grey smoke texture"></div>
    <div class="person">
      <div class="person-name">Peter Hallorand</div>
      <div class="person-title">Managing Director</div>
    </div>
    <div class="back-logo">TIDEWELL</div>
    <div class="logo-bar"></div>
    <ul class="contact">
      <li>21 Kestrel Court Thornlea 4168</li>
      <li><svg viewBox="0 0 14 12"><path d="M1 4 C4 1 10 1 13 4 L11 6 L9 4.5 L5 4.5 L3 6 Z M3 6 L11 6 L12 11 L2 11 Z"/></svg>0438 612054</li>
      <li><svg viewBox="0 0 14 12"><path d="M1 2 H13 V11 H1 Z M2 3 L7 7 L12 3" stroke="#fff" stroke-width="0.9"/></svg>tidewell@tidewellcoastal.com.au</li>
    </ul>
    <div class="website">www.tidewellcoastal.com.au</div>
  </article>
</section>

<section class="row-bottom">
  <article class="card card--front col-left">
    <div class="front-art" role="img" aria-label="Deep blue abstract background with soft light"></div>
    <div class="front-logo">TIDEWELL</div>
    <div class="front-tagline">Promotional Merchandise with a difference</div>
  </article>

  <article class="card card--back col-right">
    <div class="mist" role="img" aria-label="Soft pale grey smoke texture"></div>
    <div class="person">
      <div class="person-name">Peter Hallorand</div>
      <div class="person-title">Managing Director</div>
    </div>
    <div class="back-logo">TIDEWELL</div>
    <div class="logo-bar"></div>
    <ul class="contact">
      <li>21 Kestrel Court Thornlea 4168</li>
      <li><svg viewBox="0 0 14 12"><path d="M1 4 C4 1 10 1 13 4 L11 6 L9 4.5 L5 4.5 L3 6 Z M3 6 L11 6 L12 11 L2 11 Z"/></svg>0438 612054</li>
      <li><svg viewBox="0 0 14 12"><path d="M1 2 H13 V11 H1 Z M2 3 L7 7 L12 3" stroke="#fff" stroke-width="0.9"/></svg>tidewell@tidewellcoastal.com.au</li>
    </ul>
    <div class="website">www.tidewellcoastal.com.au</div>
  </article>
</section>

</body>
</html>
```